Web Design - Personal Item Tags Portal

web page designs need to be created for a new company that provides item tracking tags and lets users register and report stolen/found items.
The theme of the designs needs to be energetic and convey a sense of freedom and adventure - where the user does not have to worry about their items since they have all been "tagged".
the client likes parts of the site at: http://www.plimcraft.example/
they like:
1. slider images at top of pages. large slider on front page. fixed smaller height picture on internal pages
2. fixed company message on left-hand-side
3. My Account button to be clear and stand out

other comments:
clean, simple
• brand focused
• will have clear call to actions
• will include a description of what and why
• will appeal to both males and females

sections that the website will have are:
Home
About Us
How it works
Why
Case Studies
Uses and Applications
Shop
Contact Us

please create 2 designs : 1 home page, 1 internal page

Final winner will also require HTML slicing to be done.

hi, i have now updated the images so they work. sorry!

Hi, looking at all the designs that are coming in, alot of them are great. Designers need to remember to make the register for an account button more prominent. Also, there should be a "report found" and "report lost" buttons on the front-page and should be prominent as well.

Thanks

Hi, the customer has come back with a few comments and modifications for the designs, if you are able to make some tweaks to your submissions, that will be great:

The client would like the designs to be modified to highlight 3 main actions:
1. Log In/Register
2. Find an Owner
3. Lost an Item

The home page shouldnt be too content heavy in terms of text, it should only have major highlight points of what the system does (the 3 points listed above). the inner page designs are OK to have more text though.

i will also upload some notes from the customer that can be used as a guide and also include the design styles which the customer likes (but is not entirely happy with).

uploaded image files (3) with customer feedback comments

```html
<!DOCTYPE html>
<html lang="en">
<head>
<meta charset="utf-8">
<title>Wayfind</title>
<link href="https://fonts.googleapis.com/css2?family=Lato:wght@300;400;700;900&display=swap" rel="stylesheet">
<style>
:root{
  --green:#5aa11e;
  --blue:#3f9fd0;
  --blue-link:#3a8fc9;
  --navy:#1c2a4d;
  --text:#333a4a;
  --muted:#9aa0a8;
  --line:#e2e5e8;
  --sky-top:#bfe6fb;
  --sky-bottom:#78c8f1;
  --footer:#f4f4f4;
  --white:#ffffff;
}
*{box-sizing:border-box;margin:0;padding:0}
html,body{width:796px;height:1200px;overflow:hidden;background:var(--white)}
body{position:relative;font-family:Arial,Helvetica,sans-serif;color:var(--text)}
.abs{position:absolute}

/* header */
.brand{left:80px;top:25px;font-family:Lato,sans-serif;font-size:25px;font-weight:400;color:var(--blue);line-height:30px}
.btn{display:flex;align-items:center;justify-content:center;font-family:Lato,sans-serif;font-weight:700;font-size:10px;border-radius:3px}
.btn-login{left:577px;top:28px;width:63px;height:22px;background:var(--green);color:var(--white)}
.btn-register{left:657px;top:27px;width:63px;height:23px;border:1px solid var(--line);color:var(--navy);font-weight:400}
.main-nav{left:0;top:77px;width:796px;height:16px;font-family:Lato,sans-serif;font-size:11px;color:var(--navy)}
.main-nav span{position:absolute;top:0;white-space:nowrap}
.main-nav .current{color:var(--blue-link)}
.header-rule{left:0;top:104px;width:796px;height:3px;background:linear-gradient(#d7dadd,#fff)}

/* hero */
.hero{left:0;top:107px;width:796px;height:265px;background:linear-gradient(100deg,var(--sky-top),var(--sky-bottom) 60%)}
.hero-title{left:78px;top:140px;font-family:Lato,sans-serif;color:var(--navy);line-height:34px}
.hero-title strong{display:block;font-size:38px;font-weight:900}
.hero-title span{display:block;font-size:36px;font-weight:300}
.hero-lead{left:80px;top:266px;width:380px;font-family:Lato,sans-serif;font-size:10.5px;line-height:16px;color:#2f3b55}
.btn-ghost{left:80px;top:325px;width:91px;height:23px;border:1px solid var(--white);color:var(--white);gap:8px}
.pager{display:flex;width:127px;height:23px;background:var(--white);border:1px solid var(--line);border-radius:3px;font-size:11px;color:#888}
.pager i{font-style:normal;flex:1;display:flex;align-items:center;padding:0 12px}
.pager i:first-child{border-right:1px solid var(--line);flex:0 0 40px}
.pager i:last-child{justify-content:flex-end}
.hero-pager{left:593px;top:325px}
.hero-product{left:520px;top:132px;width:190px;height:128px;border-radius:10px;transform:rotate(38deg);background:linear-gradient(135deg,#2a2e33,#d9dde0 45%,#ffffff 55%,#1c1f22)}

/* why */
.why-title{left:78px;top:390px;font-family:Lato,sans-serif;font-size:23px;font-weight:700;color:var(--green)}
.why-lead{left:80px;top:436px;width:625px;font-size:9.6px;font-weight:700;line-height:20px;color:var(--navy)}
.why-list{font-size:9.6px;color:var(--blue-link);line-height:20px;list-style:none}
.why-list li::before{content:"→";color:#999;margin-right:14px}
.list-a{left:152px;top:496px}
.list-b{left:411px;top:496px}
.btn-green{background:var(--green);color:var(--white)}
.btn-about{left:333px;top:559px;width:135px;height:23px}
.section-rule{left:0;top:606px;width:796px;height:1px;background:var(--line)}

/* report tabs */
.tab{height:33px;font-family:Lato,sans-serif;font-size:12.5px;font-weight:700;display:flex;align-items:center;justify-content:center;border-radius:3px}
.tab-found{left:80px;top:632px;width:313px;background:var(--blue);color:var(--white)}
.tab-found::after{content:"";position:absolute;left:150px;bottom:-6px;border:6px solid transparent;border-bottom:0;border-top-color:var(--blue)}
.tab-lost{left:406px;top:632px;width:314px;border:1px solid var(--line);color:var(--navy)}

.report{width:151px;top:689px}
.report .tags{font-size:6.6px;color:var(--blue-link);margin-bottom:17px}
.report .tags span{margin-right:8px}
.report h3{font-size:9.6px;font-weight:700;color:var(--green);line-height:12px;text-align:justify;margin-bottom:12px}
.report .shot{height:77px;margin-bottom:17px}
.report p{font-size:8px;line-height:13.5px;text-align:justify}
.report p.strong{font-weight:700;color:var(--navy);margin-bottom:12px}
.report p.plain{color:#555}
.report .btn{width:63px;height:22px;margin-top:17px;font-size:10px;font-weight:400}
.r1{left:79px}.r2{left:242px}.r3{left:406px}.r4{left:569px}

.list-pager{left:266px;top:1047px}
.btn-more-found{left:406px;top:1047px;width:128px;height:22px;background:var(--blue);color:var(--white);font-size:9.5px}

/* footer */
.site-footer{left:0;top:1096px;width:796px;height:104px;background:var(--footer);border-top:2px solid #d5d8db}
.foot-nav{left:0;top:1121px;width:796px;height:12px;font-size:8px;color:var(--blue-link)}
.foot-nav span{position:absolute;top:0;white-space:nowrap}
.copyright{left:79px;top:1150px;font-size:8px;color:var(--text)}
.foot-note{left:79px;top:1164px;font-size:7px;line-height:10px;color:var(--muted)}
</style>
</head>
<body>

<header>
  <div class="abs brand">Wayfind</div>
  <div class="abs btn btn-login">Login</div>
  <div class="abs btn btn-register">Register</div>
  <nav class="abs main-nav">
    <span style="left:80px;top:1px"><svg width="12" height="11" viewBox="0 0 12 11"><path d="M6 0 0 5.5h1.6V11h3.2V7.5h2.4V11h3.2V5.5H12z" fill="#1c2a4d"/></svg></span>
    <span class="current" style="left:113px">About Us</span>
    <span style="left:180px">How it works</span>
    <span style="left:262px">Why</span>
    <span style="left:306px">Case Studies</span>
    <span style="left:387px">Uses and Applications</span>
    <span style="left:509px">Shop</span>
    <span style="left:555px">Contact Us</span>
  </nav>
  <div class="abs header-rule"></div>
</header>

<section>
  <div class="abs hero"></div>
  <h1 class="abs hero-title"><strong>Lorem ipsum dolor</strong><span>sit amet, consectetur</span><span>adipiscing elit.</span></h1>
  <p class="abs hero-lead">Aenean venenatis lacinia erat, vitae gravida risus tempus et. Curabitur tempor metus quis nisi varius et sodales nisi dapibus.</p>
  <div class="abs btn btn-ghost">View more <span>→</span></div>
  <div class="abs hero-product" role="img" aria-label="Black tracking tag with clear window and strap"></div>
  <div class="abs pager hero-pager"><i>←</i><i>→</i></div>
</section>

<section>
  <h2 class="abs why-title">Why Wayfind?</h2>
  <p class="abs why-lead">Mauris malesuada purus sed orci ullamcorper tempor. Nulla sit amet eros nisi. Pellentesque ornare sagittis diam, et condimentum libero molestie eget. Mauris a purus velit, non congue nunc. In elementum felis et nunc cursus sagittis:</p>
  <ul class="abs why-list list-a"><li>Praesent aliquet dui eget diam rutrum</li><li>Nullam quis sapien eros, eget rhoncus odio.</li></ul>
  <ul class="abs why-list list-b"><li>In commodo est quis enim iaculis mattis.</li><li>Integer ut tellus a diam porta pulvinar.</li></ul>
  <div class="abs btn btn-green btn-about">Read more about Wayfind</div>
  <div class="abs section-rule"></div>
</section>

<section>
  <div class="abs tab tab-found">Report found</div>
  <div class="abs tab tab-lost">Report lost</div>

  <article class="abs report r1">
    <div class="tags"><span>laoreet lectus</span><span>curabitur</span><span>metus et tortor</span></div>
    <h3>Mauris malesuada purus sed orci ullamcorper tempor.</h3>
    <div class="shot" role="img" aria-label="Tablet computer showing app icons" style="background:linear-gradient(135deg,#1e5fa8,#8fc2ea 60%,#2a6cb2)"></div>
    <p class="strong">Nulla sit amet eros nisi. Pellentesque ornare sagittis diam, et condimentum libero molestie eget. Mauris a purus velit, non congue nunc.</p>
    <p class="plain">Phasellus quis odio eu risus aliquet scelerisque sed id nulla. Nam at sem ac lectus pulvinar consectetur ut eget purus.</p>
    <div class="btn btn-green">View more</div>
  </article>

  <article class="abs report r2">
    <div class="tags"><span>laoreet lectus</span><span>curabitur</span><span>metus et tortor</span></div>
    <h3>Mauris malesuada purus sed orci ullamcorper tempor.</h3>
    <div class="shot" role="img" aria-label="Laptop with colourful tiled start screen" style="background:linear-gradient(180deg,#6a3fa0,#8a5cc0 55%,#2b2d30 80%)"></div>
    <p class="strong">Aliquam pulvinar ultricies elit, vel aliquet justo dapibus id. Vivamus ultrices congue arcu, scelerisque enim.</p>
    <p class="plain">Phasellus quis odio eu risus aliquet scelerisque sed id nulla. Nam at sem ac lectus pulvinar consectetur ut eget purus.</p>
    <div class="btn btn-green">View more</div>
  </article>

  <article class="abs report r3">
    <div class="tags"><span>laoreet lectus</span><span>curabitur</span><span>metus et tortor</span></div>
    <h3>Mauris malesuada purus sed orci ullamcorper tempor.</h3>
    <div class="shot" role="img" aria-label="White smartphone showing home screen" style="background:linear-gradient(160deg,#f2f3f5,#c9dced 50%,#e9ecef)"></div>
    <p class="strong">Cras sollicitudin metus et tortor rutrum sed faucibus mi vehicula. Etiam id eros vel lacus semper fermentum. Ut laoreet lectus a ligula porta ac hendrerit lacus varius.</p>
    <p class="plain">Cras eget lacus sem, eu gravida massa. Integer ut mauris eu mi molestie interdum nec ac est. Maecenas semper purus ac turpis tempor iaculis. Donec quis elit eget arcu iaculis egestas.</p>
    <div class="btn btn-green">View more</div>
  </article>

  <article class="abs report r4">
    <div class="tags"><span>laoreet lectus</span><span>curabitur</span><span>metus et tortor</span></div>
    <h3>Mauris malesuada purus sed orci ullamcorper tempor.</h3>
    <div class="shot" role="img" aria-label="Dark tablet showing blue desktop screen" style="background:linear-gradient(135deg,#1a1c1f 20%,#0d4f9a 50%,#3ea0e6 80%)"></div>
    <p class="strong">Nulla sit amet eros nisi. Pellentesque ornare sagittis diam, et condimentum libero molestie eget. Mauris a purus velit, non congue nunc.</p>
    <p class="plain">Phasellus quis odio eu risus aliquet scelerisque sed id nulla. Nam at sem ac lectus pulvinar consectetur ut eget purus.</p>
    <div class="btn btn-green">View more</div>
  </article>

  <div class="abs pager list-pager"><i>←</i><i>→</i></div>
  <div class="abs btn btn-more-found">View more report found</div>
</section>

<footer>
  <div class="abs site-footer"></div>
  <nav class="abs foot-nav">
    <span style="left:79px">Home</span>
    <span style="left:123px">About Us</span>
    <span style="left:179px">How it works</span>
    <span style="left:247px">Why</span>
    <span style="left:285px">Case Studies</span>
    <span style="left:357px">Uses and Applications</span>
    <span style="left:461px">Shop</span>
    <span style="left:503px">Contact Us</span>
  </nav>
  <p class="abs copyright">Copyright © 2013 Wayfind. All rights reserved.</p>
  <p class="abs foot-note">Quisque feugiat justo nec sapien feugiat vitae elementum massa sollicitudin.<br>Fusce sodales dui vel risus vulputate adipiscing in quis quam.</p>
</footer>

</body>
</html>
```